Prairie Lantern Jubilee

Organization:
Prairie Lantern Jubilee is a non-profit organization created by a group of anonymous donors to bring more fun, culture, and art to a small Texas town. Our mission is to promote art and music in Caldwell Ridge County.
The multi-day eclectic festival will feature three stages, a film, art vendors, live mural artists, and food trucks set up throughout historic downtown Oakvale. The event is FREE to the public.
Goals:
We need an attractive poster to publicize the festival.
Details:
Prairie Lantern Jubilee
Friday, October 14 – 16
Free admission (VIP tickets available)
Live music- 3 stages/10 bands
Film Screening
Art vendors and art walk
Live art murals
Food trucks
www.prairielanternjubilee.example
#prairielantern
Requirements:
Please incorporate our festival logo attached.
Conclusion:
After selecting a poster design, we hope to continue to work with the artist to design other event materials including website splash page and rack cards using design elements from the poster.

```html
<!DOCTYPE html>
<html lang="en">
<head>
<meta charset="utf-8">
<title>Prairie Lantern Jubilee – Poster</title>
<link rel="stylesheet" href="https://fonts.googleapis.com/css2?family=Alfa+Slab+One&family=Arimo:wght@700&family=Gochi+Hand&family=Marcellus&display=swap">
<style>
  :root {
    --page: #ffffff;
    --ink-black: #05070a;
    --glow-mint: #c9fbe6;
    --glow-green: #2fbf86;
    --stage-teal: #0f6a5c;
    --stage-deep: #0a2f33;
    --band-teal: #0c2d2a;
    --accent-green: #5fe08c;
    --white: #ffffff;
  }
  * { box-sizing: border-box; margin: 0; padding: 0; }
  html, body {
    width: 1200px; height: 1200px; overflow: hidden;
    background: var(--page);
  }
  .poster {
    position: absolute;
    left: 209px; top: 47px;
    width: 782px; height: 1106px;
    background: var(--ink-black);
    overflow: hidden;
  }
  .stage-photo {
    position: absolute; left: 0; top: 0;
    width: 782px; height: 857px;
    background:
      radial-gradient(ellipse 260px 220px at 420px 500px, var(--glow-mint) 0%, rgba(201,251,230,0.55) 35%, rgba(201,251,230,0) 100%),
      radial-gradient(ellipse 320px 240px at 600px 340px, rgba(180,240,230,0.8) 0%, rgba(120,210,200,0) 100%),
      radial-gradient(ellipse 520px 480px at 400px 380px, var(--glow-green) 0%, var(--stage-teal) 55%, var(--stage-deep) 100%);
  }
  .stage-photo::after {
    content: "";
    position: absolute; left: 0; right: 0; bottom: 0; height: 320px;
    background: linear-gradient(to bottom, rgba(5,7,10,0) 0%, rgba(5,7,10,0.85) 45%, var(--ink-black) 100%);
  }
  .headline {
    position: absolute; left: 0; top: 0;
    width: 782px; height: 420px;
    overflow: visible;
  }
  .festival-title {
    font-family: "Gochi Hand", cursive;
    font-size: 66px;
    fill: var(--white);
    stroke: #000; stroke-width: 2px; paint-order: stroke;
    filter: drop-shadow(3px 3px 0 #000);
  }
  .date-day {
    font-family: "Alfa Slab One", serif;
    font-size: 250px;
    fill: var(--white);
    filter: drop-shadow(4px 4px 4px rgba(0,0,0,0.55));
  }
  .date-month {
    font-family: "Alfa Slab One", serif;
    font-size: 38px;
    fill: var(--white);
    filter: drop-shadow(2px 2px 1px rgba(0,0,0,0.85));
  }
  .features {
    position: absolute; left: 0; top: 880px; width: 782px;
    text-align: center;
    font-family: "Marcellus", serif;
    font-size: 26px; line-height: 45px;
    color: var(--white);
  }
  .features .sep { color: var(--accent-green); padding: 0 6px; }
  .admission-band {
    position: absolute; left: 0; top: 989px;
    width: 782px; height: 117px;
    background: var(--band-teal);
  }
  .admission-text {
    position: absolute; left: 57px; top: 38px;
    font-family: "Arimo", sans-serif; font-weight: 700;
    font-size: 28px; line-height: 1;
    color: var(--accent-green);
  }
  .festival-mark {
    position: absolute; left: 619px; top: 11px;
    width: 100px;
    text-align: center;
  }
  .festival-mark .mark-square {
    display: block; width: 100px; height: 69px;
    background: var(--white);
  }
  .festival-mark .mark-name {
    display: block; margin-top: 6px;
    font-family: "Marcellus", serif;
    font-size: 9px; line-height: 1;
    color: var(--white);
    white-space: nowrap;
  }
</style>
</head>
<body>
  <main class="poster">
    <div class="stage-photo" role="img" aria-label="Concert photo: drummer and singer with ukulele on stage under green and white stage lights, crowd of raised hands in silhouette in the foreground"></div>

    <svg class="headline" viewBox="0 0 782 420" aria-labelledby="headline-title">
      <title id="headline-title">Prairie Lantern Jubilee, 14 October 2016</title>
      <text class="festival-title" x="51" y="104" textLength="682" lengthAdjust="spacingAndGlyphs">PRAIRIE LANTERN JUBILEE</text>
      <text class="date-day" x="119" y="337" textLength="228" lengthAdjust="spacingAndGlyphs">14</text>
      <text class="date-month" x="104" y="375" textLength="259" lengthAdjust="spacingAndGlyphs">OCTOBER 2016</text>
    </svg>

    <p class="features">
      Live music -3 stages / 10 bands<span class="sep">|</span>Film screening<br>
      Art vendors and art walk<span class="sep">|</span>Live art murals<span class="sep">|</span>Food trucks
    </p>

    <section class="admission-band">
      <p class="admission-text">FREE Admission / VIP Tickets Available</p>
      <div class="festival-mark">
        <span class="mark-square"></span>
        <span class="mark-name">PRAIRIE LANTERN JUBILEE</span>
      </div>
    </section>
  </main>
</body>
</html>
```